Harrowgate Estates Business Card for Apartment Buildings

Create business cards for resident managers who run apartment buildings. The audience is the public who are searching for apartment rentals, and current residents who live at the apartment building. Key design element will be incorporating the company logo, however, the logo cannot dominate. The building name and manager name are more important than the logo. Current business card design leaves little room for copy, so we may need to reduce the size on the current card to allow for more space for copy.

Target Market(s)

Adults 18-65 years of age, who are looking for an apartment rental, plus current residents who live at our apartment buildings.

Industry/Entity Type

Property Management

Contact Information for Business Card

A major design element will be use of the company logo. Important property and manager contact information must be part of the design. The size of the logo will need to be reduced to make room for building and manager contact copy.

Font styles to use
Sans Serif

Colors
3176b5
000000
959595
ffffff

Requirements
Must have
• 1) Incorporate the company logo.
• 2) Use the company colors (dark blue, black/grey, over white).
• 3) FEATURE THE BUILDING NAME
• 4) FEATURE THE MANAGER NAME
• 5) The company name is less important than BUILDING and MANAGER
• 6) Manager contact information
• **SEE ATTACHED CREATIVE BRIEF**
Nice to have
• 1) Back of card logo watermark
• 2) Ability to write notes on back of carfd
Should not have
• Avoid letting the company logo dominate the card, the building name and manager are more important than the company logo.

```html
<!DOCTYPE html>
<html lang="en">
<head>
<meta charset="utf-8">
<title>Harrowgate Estates – Resident Manager Card</title>
<link href="https://fonts.googleapis.com/css2?family=Lato:wght@400;700;900&display=swap" rel="stylesheet">
<style>
  :root {
    --brand-blue: #3176b5;
    --ink: #1a1a1a;
    --mid-grey: #959595;
    --white: #ffffff;
    --paper: #f1f1f1;
    --stage: #8e9194;
  }
  * { box-sizing: border-box; margin: 0; padding: 0; }
  html, body { width: 1200px; height: 1200px; overflow: hidden; }
  body {
    background: var(--stage);
    font-family: "Lato", sans-serif;
    position: relative;
  }
  .card {
    position: absolute;
    left: 140px;
    width: 920px;
    height: 495px;
    background: var(--paper);
    overflow: hidden;
    box-shadow: 0 6px 14px rgba(0,0,0,0.25);
  }
  .card--front { top: 62px; }
  .card--back { top: 630px; }

  .city-backdrop {
    position: absolute; inset: 0;
    background: linear-gradient(180deg, #f3f3f3 0%, #e4e4e4 45%, #d9d9d9 100%);
  }
  .brand-panel { position: absolute; inset: 0; width: 920px; height: 495px; }

  .building-name {
    position: absolute; left: 54px; top: 52px;
    color: var(--brand-blue);
    font-weight: 700; font-size: 35px; line-height: 41px;
    letter-spacing: 0.3px;
  }
  .address {
    position: absolute; left: 53px; top: 188px;
    display: flex; align-items: flex-start; gap: 14px;
    color: var(--ink); font-size: 19px; line-height: 25px;
  }
  .address svg { width: 28px; height: 40px; flex: none; }

  .company-mark {
    position: absolute; left: 150px; top: 370px;
    display: flex; align-items: center; gap: 10px;
    color: var(--brand-blue); font-weight: 900; font-size: 24px;
  }
  .company-mark .dot { width: 18px; height: 18px; background: var(--brand-blue); }

  .manager {
    position: absolute; left: 460px; width: 400px; top: 100px;
    text-align: center; color: var(--white);
  }
  .manager__name { font-weight: 900; font-size: 34px; line-height: 40px; }
  .manager__title {
    margin-top: 6px; font-size: 21px;
    display: flex; align-items: center; justify-content: center; gap: 12px;
  }
  .manager__title::before, .manager__title::after {
    content: ""; width: 65px; height: 2px; background: var(--white);
  }

  .contacts {
    position: absolute; left: 510px; top: 240px;
    list-style: none; color: var(--white); font-size: 24px;
  }
  .contacts li { display: flex; align-items: center; height: 36px; margin-bottom: 2px; }
  .contacts svg { width: 28px; height: 28px; margin-right: 12px; flex: none; }

  .notes-title {
    position: absolute; left: 53px; top: 92px;
    color: var(--brand-blue); font-weight: 700; font-size: 27px; letter-spacing: 0.5px;
  }
  .back-mark {
    position: absolute; left: 600px; top: 62px;
    display: flex; align-items: center; gap: 10px;
  }
  .back-mark .dot { width: 22px; height: 22px; background: var(--brand-blue); }
  .back-mark__text { color: var(--brand-blue); font-weight: 900; font-size: 25px; line-height: 1; }
  .note-line {
    position: absolute; left: 53px; width: 814px; height: 1px; background: #555;
  }
</style>
</head>
<body>

<section class="card card--front">
  <div class="city-backdrop" role="img" aria-label="Faded black and white photo of downtown high-rise towers by the bay"></div>

  <svg class="brand-panel" viewBox="0 0 920 495" aria-hidden="true">
    <path fill="#3176b5" d="M520 0 H920 V495 H440 L452 470 L446 440 L468 410 L458 380 L478 350 L466 320 L488 290 L470 262 L492 230 L474 200 L496 170 L480 140 L500 110 L486 80 L510 50 L496 22 Z"/>
  </svg>

  <h1 class="building-name">LINDEN<br>COURT<br>APARTMENTS</h1>

  <div class="address">
    <svg viewBox="0 0 28 40"><path fill="#1a1a1a" d="M14 0C6 0 0 6 0 14c0 10 14 26 14 26s14-16 14-26C28 6 22 0 14 0z"/><circle cx="14" cy="13" r="5" fill="#f1f1f1"/></svg>
    <p>2845 Crescent Avenue<br>Lakeside, CA 90210</p>
  </div>

  <div class="company-mark"><span class="dot"></span>Harrowgate Estates</div>

  <div class="manager">
    <h2 class="manager__name">MARISOL ORTEGA</h2>
    <p class="manager__title">Resident Manager</p>
  </div>

  <ul class="contacts">
    <li>
      <svg viewBox="0 0 28 28"><rect x="8" y="3" width="12" height="23" rx="2" fill="none" stroke="#fff" stroke-width="2"/><line x1="11" y1="8" x2="17" y2="8" stroke="#fff" stroke-width="2"/><path d="M11 13h2M15 13h2M11 17h2M15 17h2M11 21h2M15 21h2" stroke="#fff" stroke-width="2"/></svg>
      555-214-3087
    </li>
    <li>
      <svg viewBox="0 0 28 28"><path fill="#fff" d="M2 10c4-5 20-5 24 0l-2 4-5-1v-3c-3-1-7-1-10 0v3l-5 1z"/><path fill="#fff" d="M7 14h14l3 10H4z"/><circle cx="14" cy="19" r="3" fill="#3176b5"/></svg>
      555-306-4192
    </li>
    <li>
      <svg viewBox="0 0 28 28"><rect x="8" y="2" width="12" height="12" fill="none" stroke="#fff" stroke-width="2"/><rect x="3" y="13" width="22" height="12" rx="2" fill="none" stroke="#fff" stroke-width="2"/><path d="M7 19h14" stroke="#fff" stroke-width="2"/></svg>
      555-481-6620
    </li>
    <li>
      <svg viewBox="0 0 28 28"><rect x="3" y="7" width="22" height="15" fill="none" stroke="#fff" stroke-width="2"/><path d="M3 7l11 9 11-9M3 22l8-7M25 22l-8-7" fill="none" stroke="#fff" stroke-width="2"/></svg>
      marisol@harrowgate.com
    </li>
    <li>
      <svg viewBox="0 0 28 28"><circle cx="14" cy="14" r="11" fill="none" stroke="#fff" stroke-width="2"/><ellipse cx="14" cy="14" rx="5" ry="11" fill="none" stroke="#fff" stroke-width="2"/><path d="M3 14h22M5 8h18M5 20h18" stroke="#fff" stroke-width="2"/></svg>
      www.harrowgate.com
    </li>
  </ul>
</section>

<section class="card card--back">
  <div class="city-backdrop" role="img" aria-label="Faded black and white photo of waterfront towers and city skyline"></div>

  <div class="back-mark">
    <span class="dot"></span>
    <span class="back-mark__text">HARROWGATE ESTATES LLC</span>
  </div>

  <h2 class="notes-title">Write notes:</h2>

  <div class="note-line" style="top:178px"></div>
  <div class="note-line" style="top:237px"></div>
  <div class="note-line" style="top:291px"></div>
  <div class="note-line" style="top:349px"></div>
  <div class="note-line" style="top:408px"></div>
</section>

</body>
</html>
```